Brochure Design - Marketing Document - real estate development

It is a 7 Page Proposal document. Please see attached example. It will be used as a marketing proposal document given to potential clients. It is a 'capability statement' used to demonstrate the capability and expertise of the business. I will provide all images and copy to be used in the document. I just need someone to create the template. Use the attached document as a guide for design, style, look and feel

Company name: Tarvale Living

I'll be happy to receive the document 80% complete so I can fill in the copy and minor details. All I need from a designer is to format and design a template that I can fill in

Thank you!

Target Market(s)

Corporate investors/clients

Font styles to use
Serif
Sans Serif

Requirements
Must have
• Please use the images of elderly people I have uploaded. There doesn't need to be a photo on every page, but please incorporate the images as you see fit. Also please use the logo attached 'Tarvale Living'
• Please see below the template layout/order page by page
• 1st page
• • Branding, photo of beach, headline saying capability statement
• 2nd page
• ABOUT US
• • High level overview from market/retail perspective of what Tarvale offers and who we are
• • Talk about product and company philosophy
• 3rd page
• OUR TEAM
• • Photos, names and roles
• • Speak generally about immense team experience as a composite body of achievement
• 4th Page
• • List of projects and project values
• Page 5
• • More projects and project values
• Page 6
• • What we are offering our JV partners
• • Benefits and options of model
• Page 7
• • How Tarvle will change the market for the better/ difference between us and old models
• Final page
• • Branding, Address, company details. ABN/CAN
Should not have
• Please do NOT use bright/electric colours of blue, green or orange.
• Please use the attached document as a guide for style, colours and layout

```html
<!DOCTYPE html>
<html lang="en">
<head>
<meta charset="utf-8">
<title>Tarvale Living – Capability Statement Template</title>
<link href="https://fonts.googleapis.com/css2?family=Oswald:wght@400;500;600&family=Open+Sans:wght@400;600;700&family=Cormorant+Garamond:wght@500&display=swap" rel="stylesheet">
<style>
:root{
  --stage:#1f1f1f;
  --teal:#1f4a51;
  --teal-deep:#173a40;
  --tan:#b99b6d;
  --paper:#ffffff;
  --ink:#2a2a2a;
  --muted:#e6ecec;
  --ring:#f2e23a;
}
*{box-sizing:border-box;margin:0;padding:0}
html,body{width:1200px;height:1200px;overflow:hidden;background:var(--stage)}
body{position:relative;font-family:"Open Sans",Arial,sans-serif;color:var(--ink)}
.page{position:absolute;background:var(--paper);overflow:hidden}
.abs{position:absolute}
.photo{position:absolute}
.body-copy{font-size:3.6px;line-height:1.45;text-align:justify}
.light{color:var(--muted)}
.footer{position:absolute;left:0;right:0;bottom:0;height:20px;background:var(--tan)}
.footer .url{position:absolute;left:22px;top:7px;font-size:3.8px;font-weight:700;color:#fff}
.footer .tag{position:absolute;right:0;top:0;width:42px;height:20px;background:#fff;clip-path:polygon(18% 0,100% 0,100% 100%,0 100%);font-size:3.8px;font-weight:700;text-align:center;line-height:20px;padding-left:8px;color:var(--ink)}
.wordmark{font-family:"Cormorant Garamond",Georgia,serif;font-weight:500;letter-spacing:.18em;text-align:center}
.head{font-family:"Oswald",Arial,sans-serif;font-weight:500}

/* page positions */
.p1{left:37px;top:206px;width:258px;height:362px}
.p2{left:330px;top:208px;width:254px;height:358px;background:var(--teal)}
.p3{left:626px;top:210px;width:257px;height:359px}
.p4{left:914px;top:213px;width:254px;height:355px}
.p5{left:49px;top:652px;width:254px;height:356px}
.p6{left:333px;top:652px;width:254px;height:357px}
.p7{left:628px;top:652px;width:255px;height:359px;background:var(--teal)}
.p8{left:914px;top:651px;width:258px;height:363px;background:var(--tan)}

/* page 1 */
.p1 .wordmark{position:absolute;top:10px;left:0;right:0;font-size:16px;color:#7c7c7c}
.cover-block{position:absolute;left:0;right:0;top:235px;height:98px;background:var(--teal)}
.cover-title{position:absolute;left:13px;top:10px;font-size:25.5px;font-weight:600;color:#fff;letter-spacing:-.2px;white-space:nowrap}
.cover-block .body-copy{position:absolute;left:13px;right:13px;top:51px;color:#fff}
.p1 .footer{height:29px}
.p1 .footer .url{left:0;right:0;text-align:center;top:9px;font-size:8px}

/* page 2 */
.tab{position:absolute;left:104px;top:160px;width:50px;height:17px;background:var(--tan);border-radius:6px 6px 0 0;color:#fff;font-size:11px;text-align:center;line-height:17px}
.sub-head{position:absolute;left:18px;color:#fff;font-size:9px;line-height:1.35}
.rule{position:absolute;height:1px;background:#fff}
.bullets{position:absolute;left:18px;right:20px;list-style:none}
.bullets li{position:relative;padding-left:5px;margin-bottom:4px;color:#fff}
.bullets li::before{content:"";position:absolute;left:0;top:1.6px;width:2px;height:2px;border-radius:50%;background:#fff}

/* page 3 */
.team-head{position:absolute;left:0;right:0;top:0;height:50px;background:var(--teal);text-align:center;color:#fff}
.team-head h2{font-size:15px;margin-top:13px;line-height:1}
.team-head p{font-size:8.3px;margin-top:3px}
.team-rail{position:absolute;left:0;top:60px;width:84px;bottom:20px;background:var(--teal)}
.member{position:absolute;left:14px;width:56px;text-align:center}
.avatar{width:52px;height:52px;border-radius:50%;background:var(--tan);border:2px solid #fff;margin:0 auto}
.member span{display:block;font-size:3.6px;color:#fff;line-height:1.5;margin-top:2px}
.team-copy{position:absolute;left:89px;right:13px;top:73px}
.team-copy p{margin-bottom:8px}

/* page 4 */
.list-title{position:absolute;left:0;right:0;top:10px;text-align:center;font-size:12.5px;color:var(--ink)}
.list-title::after{content:"";display:block;width:164px;height:1px;background:var(--ink);margin:2px auto 0}
.project{position:absolute;left:20px;right:24px;height:22px}
.num{position:absolute;left:0;top:0;width:15px;height:15px;border-radius:50%;background:var(--teal);color:#fff;font-family:"Oswald",Arial,sans-serif;font-weight:600;font-size:9px;text-align:center;line-height:15px}
.project .body-copy{position:absolute;left:20px;right:0;top:0}

/* page 5 */
.gallery-rail{position:absolute;left:0;top:0;width:101px;bottom:26px;background:var(--teal)}
.thumb{position:absolute;left:7px;width:88px;height:63px}
.feature{position:absolute;left:108px;right:10px}
.feature h3{font-size:6.5px;font-weight:600;margin-bottom:3px}

/* page 6 */
.offer-panel{position:absolute;left:0;top:0;width:145px;height:158px;background:rgba(31,74,81,.93);padding:22px 5px 0 8px}
.offer-panel .bullets{position:static}
.offer-panel .bullets li{margin-bottom:7px}
.offers-box{position:absolute;left:150px;top:48px;width:104px;height:45px;background:var(--tan);color:#fff;font-family:"Oswald",Arial,sans-serif;font-weight:600;font-size:16px;line-height:.95;padding:8px 0 0 8px}
.jv-label{position:absolute;left:48px;right:48px;top:317px;height:9px;border-radius:5px;background:var(--teal);color:#fff;font-size:5.5px;text-align:center;line-height:9px}
.jv-label::before,.jv-label::after{content:"";position:absolute;top:4px;width:46px;height:1px;background:#fff}
.jv-label::before{left:10px}.jv-label::after{right:10px}

/* page 7 */
.circle-photo{position:absolute;left:137px;top:115px;width:108px;height:108px;border-radius:50%;border:4px solid var(--ring);background:radial-gradient(circle at 45% 45%,#c9b9a3,#8a6c52 70%)}
.ring-line{position:absolute;left:0;top:168px;width:138px;height:3px;background:var(--ring)}
.market-head{position:absolute;left:13px;top:188px;color:#fff;font-size:12px;line-height:1.15}
.ticks{position:absolute;left:7px;right:8px;top:240px;list-style:none}
.ticks li{position:relative;padding-left:11px;margin-bottom:9px;color:#fff;font-size:4.8px;line-height:1.4}
.ticks svg{position:absolute;left:0;top:1px}

/* page 8 */
.p8 .wordmark{position:absolute;top:251px;left:0;right:0;font-size:17.5px;color:#fff}
.contact{position:absolute;left:0;right:0;text-align:center;color:#fff;font-size:4.8px;font-weight:700}
.base-strip{position:absolute;left:0;right:0;bottom:0;height:6px;background:var(--teal)}
</style>
</head>
<body>

<!-- Cover -->
<section class="page p1">
  <div class="wordmark">TARVALE LIVING</div>
  <div class="photo" role="img" aria-label="Group of smiling seniors splashing together at the beach edge" style="left:0;right:0;top:46px;height:189px;background:linear-gradient(180deg,#fff 0%,#9fbdd6 18%,#5e8fb7 42%,#8eb4c6 55%,#d9cdb8 80%,#c8b59a 100%)"></div>
  <div class="cover-block">
    <h1 class="cover-title head">CAPABILITY STATEMENT</h1>
    <p class="body-copy">Lorem ipsum dolor sit amet, consectetur adipiscing elit, sed do eiusmod tempor incididunt ut labore et dolore magna aliqua. Ut enim ad minim veniam, quis nostrud exercitation ullamco laboris nisi ut aliquip ex ea commodo consequat. Duis aute irure dolor in reprehenderit in voluptate velit esse cillum dolore eu fugiat nulla pariatur. Excepteur sint occaecat cupidatat non proident, sunt in culpa qui officia deserunt mollit anim id est laborum.</p>
  </div>
  <div class="footer"><span class="url">www.tarvaleliving.com</span></div>
</section>

<!-- About us -->
<section class="page p2">
  <div class="photo" role="img" aria-label="Senior couple laughing together on a golf course" style="left:0;right:0;top:0;height:177px;background:linear-gradient(135deg,#d8e3a7 0%,#b9cf86 40%,#e3d6b5 70%,#a9c07a 100%)"></div>
  <div class="tab head">About Us</div>
  <h2 class="sub-head head" style="top:185px;font-weight:400">Retail perspective of what Tarvale offers and who<br>we are</h2>
  <div class="rule" style="left:48px;width:80px;top:206px"></div>
  <ul class="bullets body-copy" style="top:218px">
    <li>Lorem ipsum dolor sit amet, consectetur adipiscing elit, sed do eiusmod tempor incididunt ut labore et dolore magna aliqua.</li>
    <li>Lorem ipsum dolor sit amet, consectetur adipiscing elit, sed do eiusmod tempor incididunt ut labore et dolore magna aliqua.</li>
    <li>Lorem ipsum dolor sit amet, consectetur adipiscing elit, sed do eiusmod tempor incididunt ut labore et dolore magna aliqua.</li>
  </ul>
  <h2 class="sub-head head" style="top:264px;font-weight:400">About product and company philosophy</h2>
  <div class="rule" style="left:18px;width:158px;top:278px"></div>
  <div class="abs body-copy light" style="left:18px;right:14px;top:283px">
    <p style="margin-bottom:5px">Lorem ipsum dolor sit amet, consectetur adipiscing elit, sed do eiusmod tempor incididunt ut labore et dolore magna aliqua. Ut enim ad minim veniam, quis nostrud exercitation ullamco laboris nisi ut aliquip ex ea commodo consequat. Duis aute irure dolor in reprehenderit in voluptate velit esse cillum dolore eu fugiat nulla pariatur.</p>
    <p>Lorem ipsum dolor sit amet, consectetur adipiscing elit, sed do eiusmod tempor incididunt ut labore et dolore magna aliqua. Ut enim ad minim veniam, quis nostrud exercitation ullamco laboris nisi ut aliquip ex ea commodo consequat. Duis aute irure dolor in reprehenderit in voluptate velit esse cillum dolore.</p>
  </div>
  <div class="footer"><span class="url">www.tarvaleliving.com</span><span class="tag">Page 2</span></div>
</section>

<!-- Our team -->
<section class="page p3">
  <header class="team-head">
    <h2 class="head">Our Team</h2>
    <p>Team Experience as a Composite Body of Achievement</p>
  </header>
  <div class="team-rail">
    <div class="member" style="top:12px"><div class="avatar" role="img" aria-label="Team member portrait"></div><span>Lorem Ipsum<br>Lorem Ipsum</span></div>
    <div class="member" style="top:82px"><div class="avatar" role="img" aria-label="Team member portrait"></div><span>Lorem Ipsum<br>Lorem Ipsum</span></div>
    <div class="member" style="top:152px"><div class="avatar" role="img" aria-label="Team member portrait"></div><span>Lorem Ipsum<br>Lorem Ipsum</span></div>
    <div class="member" style="top:222px"><div class="avatar" role="img" aria-label="Team member portrait"></div><span>Lorem Ipsum<br>Lorem Ipsum</span></div>
  </div>
  <div class="team-copy body-copy">
    <p>Lorem ipsum dolor sit amet, consectetur adipiscing elit, sed do eiusmod tempor incididunt ut labore et dolore magna aliqua. Ut enim ad minim veniam, quis nostrud exercitation ullamco laboris nisi ut aliquip ex ea commodo consequat. Duis aute irure dolor in reprehenderit in voluptate velit esse cillum dolore eu fugiat nulla pariatur. Excepteur sint occaecat cupidatat non proident, sunt in culpa qui officia deserunt mollit anim id est laborum.</p>
    <p>Lorem ipsum dolor sit amet, consectetur adipiscing elit, sed do eiusmod tempor incididunt ut labore et dolore magna aliqua. Ut enim ad minim veniam, quis nostrud exercitation ullamco laboris nisi ut aliquip ex ea commodo consequat. Duis aute irure dolor in reprehenderit in voluptate velit esse cillum dolore eu fugiat nulla pariatur. Excepteur sint occaecat cupidatat non proident, sunt in culpa qui officia deserunt mollit anim id est laborum.</p>
    <p>Lorem ipsum dolor sit amet, consectetur adipiscing elit, sed do eiusmod tempor incididunt ut labore et dolore magna aliqua. Ut enim ad minim veniam, quis nostrud exercitation ullamco laboris nisi ut aliquip ex ea commodo consequat. Duis aute irure dolor in reprehenderit in voluptate velit esse cillum dolore eu fugiat nulla pariatur. Excepteur sint occaecat cupidatat non proident, sunt in culpa qui officia deserunt mollit anim id est laborum.</p>
  </div>
  <div class="photo" role="img" aria-label="Team group photo of staff in business attire" style="left:84px;right:0;top:238px;bottom:20px;background:linear-gradient(180deg,#dfe3e6 0%,#b7bcc0 45%,#3a3d42 75%,#24262a 100%)"></div>
  <div class="footer"><span class="url">www.tarvaleliving.com</span><span class="tag">Page 3</span></div>
</section>

<!-- Projects -->
<section class="page p4">
  <h2 class="list-title head">List of projects and project values</h2>
  <div class="project" style="top:34px"><span class="num">1</span><p class="body-copy">Lorem ipsum dolor sit amet, consectetur adipiscing elit, sed do eiusmod tempor incididunt ut labore et dolore magna aliqua. Ut enim ad minim veniam, quis nostrud exercitation ullamco laboris nisi ut aliquip ex ea commodo consequat. Duis aute irure dolor in reprehenderit in voluptate velit esse cillum dolore.</p></div>
  <div class="project" style="top:63px"><span class="num">2</span><p class="body-copy">Lorem ipsum dolor sit amet, consectetur adipiscing elit, sed do eiusmod tempor incididunt ut labore et dolore magna aliqua. Ut enim ad minim veniam, quis nostrud exercitation ullamco laboris nisi ut aliquip ex ea commodo consequat. Duis aute irure dolor in reprehenderit in voluptate velit esse cillum dolore.</p></div>
  <div class="project" style="top:93px"><span class="num">3</span><p class="body-copy">Lorem ipsum dolor sit amet, consectetur adipiscing elit, sed do eiusmod tempor incididunt ut labore et dolore magna aliqua. Ut enim ad minim veniam, quis nostrud exercitation ullamco laboris nisi ut aliquip ex ea commodo consequat. Duis aute irure dolor in reprehenderit in voluptate velit esse cillum dolore.</p></div>
  <div class="project" style="top:125px"><span class="num">4</span><p class="body-copy">Lorem ipsum dolor sit amet, consectetur adipiscing elit, sed do eiusmod tempor incididunt ut labore et dolore magna aliqua. Ut enim ad minim veniam, quis nostrud exercitation ullamco laboris nisi ut aliquip ex ea commodo consequat. Duis aute irure dolor in reprehenderit in voluptate velit esse cillum dolore.</p></div>
  <div class="project" style="top:156px"><span class="num">5</span><p class="body-copy">Lorem ipsum dolor sit amet, consectetur adipiscing elit, sed do eiusmod tempor incididunt ut labore et dolore magna aliqua. Ut enim ad minim veniam, quis nostrud exercitation ullamco laboris nisi ut aliquip ex ea commodo consequat. Duis aute irure dolor in reprehenderit in voluptate velit esse cillum dolore.</p></div>
  <div class="photo" role="img" aria-label="Senior couple sitting together on a sunny beach" style="left:0;right:0;top:180px;bottom:20px;background:linear-gradient(180deg,#fff 0%,#a9c9df 20%,#3f85bd 45%,#2b6fa8 65%,#b9a98f 88%,#a89478 100%)"></div>
  <div class="footer"><span class="url">www.tarvaleliving.com</span><span class="tag">Page 4</span></div>
</section>

<!-- More projects -->
<section class="page p5">
  <div class="gallery-rail">
    <div class="thumb" role="img" aria-label="Senior couple cycling in a park" style="top:9px;background:linear-gradient(180deg,#8dbb5a,#cfd9a8 60%,#9aa37c)"></div>
    <div class="thumb" role="img" aria-label="Senior man at an indoor swimming pool" style="top:90px;background:linear-gradient(180deg,#cfe2f2,#3e8fd0 55%,#1f63a6)"></div>
    <div class="thumb" role="img" aria-label="Senior couple embracing outdoors" style="top:171px;background:linear-gradient(180deg,#cfe0ea,#9fb28f 60%,#6b7c5f)"></div>
    <div class="thumb" role="img" aria-label="Senior couple walking in autumn" style="top:252px;background:linear-gradient(135deg,#d89a3a,#a85a2b 50%,#3b4f74)"></div>
  </div>
  <div class="feature" style="top:14px"><h3>LOREM IPSUM GENERATOR</h3><p class="body-copy">Lorem ipsum dolor sit amet, consectetur adipiscing elit, sed do eiusmod tempor incididunt ut labore et dolore magna aliqua. Ut enim ad minim veniam, quis nostrud exercitation ullamco laboris nisi ut aliquip ex ea commodo consequat. Duis aute irure dolor in reprehenderit in voluptate velit esse cillum dolore eu fugiat nulla pariatur. Excepteur sint occaecat cupidatat non proident, sunt in culpa qui officia deserunt mollit anim id est laborum.</p></div>
  <div class="feature" style="top:79px"><h3>LOREM IPSUM GENERATOR</h3><p class="body-copy">Lorem ipsum dolor sit amet, consectetur adipiscing elit, sed do eiusmod tempor incididunt ut labore et dolore magna aliqua. Ut enim ad minim veniam, quis nostrud exercitation ullamco laboris nisi ut aliquip ex ea commodo consequat. Duis aute irure dolor in reprehenderit in voluptate velit esse cillum dolore eu fugiat nulla pariatur. Excepteur sint occaecat cupidatat non proident, sunt in culpa qui officia deserunt mollit anim id est laborum.</p></div>
  <div class="feature" style="top:146px"><h3>LOREM IPSUM GENERATOR</h3><p class="body-copy">Lorem ipsum dolor sit amet, consectetur adipiscing elit, sed do eiusmod tempor incididunt ut labore et dolore magna aliqua. Ut enim ad minim veniam, quis nostrud exercitation ullamco laboris nisi ut aliquip ex ea commodo consequat. Duis aute irure dolor in reprehenderit in voluptate velit esse cillum dolore eu fugiat nulla pariatur. Excepteur sint occaecat cupidatat non proident, sunt in culpa qui officia deserunt mollit anim id est laborum.</p></div>
  <div class="feature" style="top:211px"><h3>LOREM IPSUM GENERATOR</h3><p class="body-copy">Lorem ipsum dolor sit amet, consectetur adipiscing elit, sed do eiusmod tempor incididunt ut labore et dolore magna aliqua. Ut enim ad minim veniam, quis nostrud exercitation ullamco laboris nisi ut aliquip ex ea commodo consequat. Duis aute irure dolor in reprehenderit in voluptate velit esse cillum dolore eu fugiat nulla pariatur. Excepteur sint occaecat cupidatat non proident, sunt in culpa qui officia deserunt mollit anim id est laborum.</p></div>
  <div class="feature" style="top:276px"><h3>LOREM IPSUM GENERATOR</h3><p class="body-copy">Lorem ipsum dolor sit amet, consectetur adipiscing elit, sed do eiusmod tempor incididunt ut labore et dolore magna aliqua. Ut enim ad minim veniam, quis nostrud exercitation ullamco laboris nisi ut aliquip ex ea commodo consequat. Duis aute irure dolor in reprehenderit in voluptate velit esse cillum dolore eu fugiat nulla pariatur. Excepteur sint occaecat cupidatat non proident, sunt in culpa qui officia deserunt mollit anim id est laborum.</p></div>
  <div class="footer"><span class="url">www.tarvaleliving.com</span><span class="tag">Page 5</span></div>
</section>

<!-- Offers -->
<section class="page p6">
  <div class="photo" role="img" aria-label="Older man with a pipe looking out beside a stone monument under a cloudy sky" style="left:0;right:0;top:0;bottom:20px;background:linear-gradient(180deg,#6c6f72 0%,#9a9c9c 35%,#c9c6bd 55%,#7e7a73 75%,#3e3b38 100%)"></div>
  <div class="offer-panel">
    <ul class="bullets body-copy">
      <li>Lorem ipsum dolor sit amet, consectetur adipiscing elit, sed do eiusmod tempor incididunt ut labore et dolore magna</li>
      <li>Lorem ipsum dolor sit amet, consectetur adipiscing elit, sed do eiusmod tempor incididunt ut labore et dolore magna aliqua. Ut enim ad minim veniam, quis nostrud exercitation ullamco laboris nisi ut aliquip ex ea commodo consequat. Duis aute irure dolor in reprehenderit in voluptate velit esse cillum dolore eu fugiat nulla pariatur.</li>
      <li>Lorem ipsum dolor sit amet, consectetur adipiscing elit, sed do eiusmod tempor incididunt ut labore et dolore magna aliqua. Ut enim ad minim veniam, quis nostrud exercitation ullamco laboris nisi ut aliquip ex ea commodo consequat. Duis aute irure dolor in reprehenderit in voluptate velit esse cillum dolore eu fugiat nulla pariatur. Excepteur sint occaecat cupidatat non proident, sunt in culpa qui officia deserunt mollit anim id est laborum.</li>
    </ul>
  </div>
  <h2 class="offers-box">OUR<br>OFFERS</h2>
  <div class="jv-label">Our JV Partners</div>
  <div class="footer"><span class="url">www.tarvaleliving.com</span><span class="tag">Page 6</span></div>
</section>

<!-- Market change -->
<section class="page p7">
  <div class="photo" role="img" aria-label="Senior couple embracing while looking over a misty coastline" style="left:0;right:0;top:0;height:170px;background:linear-gradient(160deg,#c9d2cc 0%,#9fae9c 35%,#6f8267 60%,#4b5a49 100%)"></div>
  <div class="ring-line"></div>
  <div class="circle-photo" role="img" aria-label="Senior couple sharing a meal at home"></div>
  <h2 class="market-head head" style="font-weight:400">How Tarvle will change<br>the market for the better</h2>
  <ul class="ticks">
    <li><svg width="6" height="5" viewBox="0 0 6 5"><path d="M.5 2.5l1.7 1.7L5.5.6" fill="none" stroke="#fff" stroke-width="1"/></svg>Lorem ipsum, or lipsum as it is sometimes known, is dummy text used in laying out print, graphic or web designs. The passage is attributed to an unknown typesetter in the 15th century who is thought to have scrambled parts of Cicero's De Finibus Bonorum et Malorum for use in a type specimen book.</li>
    <li><svg width="6" height="5" viewBox="0 0 6 5"><path d="M.5 2.5l1.7 1.7L5.5.6" fill="none" stroke="#fff" stroke-width="1"/></svg>Lorem ipsum, or lipsum as it is sometimes known, is dummy text used in laying out print, graphic or web designs. The passage is attributed to an unknown typesetter in the 15th century who is thought to have scrambled parts of Cicero's De Finibus Bonorum et Malorum for use in a type specimen book.</li>
    <li><svg width="6" height="5" viewBox="0 0 6 5"><path d="M.5 2.5l1.7 1.7L5.5.6" fill="none" stroke="#fff" stroke-width="1"/></svg>Lorem ipsum, or lipsum as it is sometimes known, is dummy text used in laying out print, graphic or web designs. The passage is attributed to an unknown typesetter in the 15th century who is thought to have scrambled parts of Cicero's De Finibus Bonorum et Malorum for use in a type specimen book.</li>
  </ul>
  <div class="footer"><span class="url">www.tarvaleliving.com</span><span class="tag">Page 7</span></div>
</section>

<!-- Back cover -->
<section class="page p8">
  <div class="photo" role="img" aria-label="Senior couple smiling at each other, teal-toned portrait" style="left:0;right:0;top:0;height:236px;background:linear-gradient(135deg,#123238 0%,#2d5a60 40%,#7fa3a6 60%,#24474d 100%)"></div>
  <div class="wordmark">TARVALE LIVING</div>
  <svg class="abs" style="left:124px;top:293px" width="10" height="13" viewBox="0 0 10 13"><path d="M5 12.5S1 7.6 1 4.8A4 4 0 0 1 9 4.8C9 7.6 5 12.5 5 12.5z" fill="var(--teal)"/><circle cx="5" cy="4.8" r="1.5" fill="#fff"/></svg>
  <p class="contact" style="top:310px">Lorem ipsum dolor sit amet, consectetur adipiscing elit.</p>
  <svg class="abs" style="left:124px;top:322px" width="9" height="9" viewBox="0 0 9 9"><circle cx="4.5" cy="4.5" r="4" fill="var(--teal)"/><path d="M.5 4.5h8M4.5.5v8M4.5.5c-2 2.4-2 5.6 0 8M4.5.5c2 2.4 2 5.6 0 8" fill="none" stroke="#fff" stroke-width=".5"/></svg>
  <p class="contact" style="top:335px">www.tarvaleliving.com</p>
  <div class="base-strip"></div>
</section>

</body>
</html>
```